Microsite for a private healthcare provider

The design I need (PSD file) is for a company offering two services:
1. Recruitment of nurses
2. Provider a private health care: prenatal classes, vaccines for travellers
Here's a website we designed and we would like a similar style in terms of layout. Please note there will be about the same amount of content (text) http://lumeravisuel.example/fr
Main menu with 4 sections:
Accueil |Agence de placement | Soins privés | Contact
Links to their social media accounts:
https://chirpline.example/Valdoriel
https://friendwall.example/valdoriel-agence-de-placement
Contact details:
TÉL. (555) 302-4419
TÉLEC. (555) 302-9154
1187 boulevard Ormelande, suite 3400
St-Hubert (Québec), K8W 5M3
Target Market(s)
Nurses looking for a job, Expecting women, People about to travel and seeking vaccines
Industry/Entity Type
Healthcare
Requirements
Must have
- 1- Must be responsive for mobiles and tablets
2 - Twitter feed
3 - Google maps at the end next to their contact details
4- Two contact forms:
Form for people to send in their resume.
The form title is: Postulez
Fields required:
Nom complet
Courriel
Téléphone
Années d'expérience (with drop down list: 1-2 ans, 3-5 ans, 5 ans et plus)
Choose file (possibility to attach a cv)
Message
Form for requesting information
Form title is: Demande d'informations
Fields are:
Nom complet
Téléphone
Courriel
Message
Nice to have
- Here are some images on Pixvane Images the client likes, you can use for inspiration.
Agence de placement section:
File #40581936
File #6417283
File #8250946
File #5092734
File #47306152
File #39847201
File #26415037
Soins privés section:
File #33782519
File #31940285
File #34617092
File #48053276
File #27360458
File #29518064
File #42870315
File #6783052
File #35104827

```html
<!DOCTYPE html>
<html lang="fr">
<head>
<meta charset="utf-8">
<title>Valdoriel – Soins de santé personnalisés</title>
<link rel="stylesheet" href="https://fonts.googleapis.com/css2?family=Didact+Gothic&family=Arimo:wght@400;700&display=swap">
<style>
:root{
  --navy:#0d2a7a;
  --olive-dark:#5c7410;
  --olive-light:#8fa52c;
  --nav-top:#0a6f9c;
  --nav-light:#35b8ea;
  --nav-dark:#1596cf;
  --nav-text:#1e3a4c;
  --panel:#eef7fb;
  --text:#333b40;
  --ink:#111;
  --link:#1a1ad6;
  --caption-bg:rgba(40,40,40,.86);
  --social-one:#3b67b0;
  --social-two:#4bb8e6;
  --white:#fff;
}
*{margin:0;padding:0;box-sizing:border-box}
html,body{width:1200px;height:972px;overflow:hidden;background:var(--white)}
body{position:relative;font-family:"Didact Gothic",sans-serif;color:var(--text)}
a{text-decoration:none;color:inherit}

.site-header{position:absolute;left:0;top:0;width:1200px;height:116px;background:var(--white);overflow:hidden}
.header-backdrop{position:absolute;left:290px;top:-14px;font-size:110px;color:#ececec;white-space:nowrap}
.brand{position:absolute;left:15px;top:8px;width:339px;height:103px;border:1px solid #f0f0f0;background:var(--white);padding:14px 0 0 14px}
.brand-name{display:block;font-size:46px;line-height:52px;color:var(--navy)}
.brand-tagline{display:block;font-size:14px;color:var(--navy);margin-top:4px}
.utility-links{position:absolute;right:49px;top:6px;font-size:17px;color:var(--ink)}
.utility-links span{margin:0 6px}
.search{position:absolute;left:910px;top:34px;width:249px;height:37px;border:1px solid #8a8a8a;background:var(--white);display:flex;align-items:center}
.search svg{margin:0 12px 0 4px}
.search span{font-size:18px;color:#777;font-family:"Arimo",sans-serif}

.main-nav{position:absolute;left:0;top:116px;width:1200px;height:65px;border-top:3px solid var(--nav-top);background:linear-gradient(var(--nav-light),var(--nav-dark))}
.main-nav ul{list-style:none;display:flex;align-items:center;height:62px;padding-left:117px;font-size:32px;color:var(--nav-text)}
.main-nav li.sep{margin:0 24px 0 26px}
.main-nav li.sep.wide{margin:0 36px 0 38px}
.main-nav li.sep.last{margin:0 22px 0 32px}
.main-nav li.current{color:var(--white)}

.hero{position:absolute;left:0;top:181px;width:737px;height:491px}
.hero-photo{position:absolute;inset:0;background:linear-gradient(115deg,#c7d3d0 0%,#5d90a8 30%,#93b5b2 55%,#eef1ee 80%,#d8dcdc 100%)}
.hero-caption{position:absolute;left:0;top:364px;width:737px;height:127px;background:var(--caption-bg);color:var(--white);font-family:"Arimo",sans-serif;font-size:25px;line-height:30px;text-align:center;padding:23px 22px 0 0}
.slider-dots{position:absolute;left:307px;top:456px;display:flex;gap:6px}
.slider-dots span{width:20px;height:20px;border-radius:50%;border:2px solid #ddd;background:#222}
.slider-dots span.active{background:#ddd}

.content-panel{position:absolute;left:737px;top:181px;width:463px;height:701px;background:var(--panel)}
.intro{position:absolute;left:737px;top:181px;width:463px;height:491px;border-left:1px solid #8fcf7a}
.intro-title{position:absolute;left:0;top:40px;width:438px;text-align:center;font-size:25px;line-height:30px;font-weight:400;color:var(--text)}
.intro-body{position:absolute;left:17px;top:118px;width:405px;font-size:16px;line-height:19.2px;text-align:justify;letter-spacing:.2px}
.intro-body p{margin-bottom:19.2px}
.intro-body p.tight,.intro-body p.last{margin-bottom:0}
.indent{text-indent:36px}
.see-more{display:block;text-align:right;color:var(--link);line-height:19.2px;margin-top:1px}

.news{position:absolute;left:0;top:672px;width:737px;height:210px;background:var(--panel)}
.news h2{position:absolute;left:0;top:4px;width:704px;text-align:center;font-size:25px;font-weight:400;color:var(--ink)}
.news-item{position:absolute;text-align:justify;color:var(--ink);overflow:hidden}
.news-item.first{left:15px;top:36px;width:337px;height:115px;font-size:16px;line-height:19px;letter-spacing:.2px}
.news-item.second{left:406px;top:37px;width:320px;height:108px;font-size:18.5px;line-height:21.5px}
.read-more{position:absolute;top:172px;font-size:17px;color:var(--link)}
.read-more.first{left:239px}
.read-more.second{left:644px}

.site-footer{position:absolute;left:0;top:882px;width:1200px;height:90px;background:linear-gradient(var(--olive-dark),var(--olive-light));border-top:2px solid #4e5f1a;box-shadow:0 -6px 12px rgba(0,0,0,.12);color:var(--white)}
.copyright{position:absolute;left:24px;top:28px;font-size:17px;line-height:19px}
.copyright strong{font-weight:700;font-family:"Arimo",sans-serif;font-size:16px}
.footer-contact-label{position:absolute;left:684px;top:17px;font-size:18px}
.footer-contact{position:absolute;left:788px;top:14px;font-size:12px;line-height:14.5px;font-style:normal}
.social{position:absolute;left:1033px;top:8px;font-size:17px}
.social-links{display:flex;gap:4px;margin:9px 0 0 57px}
.social-links a{width:39px;height:39px;border-radius:6px;background:var(--social-one);border:1px solid #dfe8f5}
.social-links a.second{background:var(--social-two)}
</style>
</head>
<body>
<header class="site-header">
  <div class="header-backdrop" aria-hidden="true">Valdoriel</div>
  <a class="brand" href="#">
    <span class="brand-name">Valdoriel</span>
    <span class="brand-tagline">Soins de santé personnalisés, en privé</span>
  </a>
  <div class="utility-links"><a href="#">help</a><span>|</span><a href="#">support</a></div>
  <div class="search">
    <svg width="30" height="30" viewBox="0 0 30 30" aria-hidden="true"><circle cx="12" cy="12" r="8.5" fill="none" stroke="#111" stroke-width="2.5"/><line x1="18" y1="18" x2="27" y2="27" stroke="#111" stroke-width="3.5" stroke-linecap="round"/></svg>
    <span>Search here...</span>
  </div>
</header>

<nav class="main-nav">
  <ul>
    <li class="current">Accueil</li><li class="sep">|</li>
    <li>Agence de placement</li><li class="sep wide">|</li>
    <li>Soins privés</li><li class="sep last">|</li>
    <li>Contact</li>
  </ul>
</nav>

<section class="hero">
  <div class="hero-photo" role="img" aria-label="Photo d'une infirmière souriante au chevet d'un patient âgé à l'hôpital"></div>
  <div class="hero-caption">“AMERICA'S NURSING SHORTAGE - THE NEED FOR<br>INTERNATIONAL NURSES!”</div>
  <div class="slider-dots"><span class="active"></span><span></span><span></span><span></span><span></span></div>
</section>

<div class="content-panel"></div>
<section class="intro">
  <h1 class="intro-title">Microsite for a private<br>healthcare provider</h1>
  <div class="intro-body">
    <p class="tight indent">Dummy Text. The United States is currently experiencing a shortage of nurses. It has been estimated that by the year 2020, that deficit can grow to up to 1 Million vacancies. To try and avert this crisis, US hospitals are increasingly looking overseas to recruit for international nurses.</p>
    <p>This Directory of International Nurse Recruiters is intended to bring together, in one place, a listing of all the international nurse recruiters and assist foreign educated nurses to find jobs in the USA. The list is divided between Staffing Agencies, also known as International Nurse Recruiters, and Law Firms that specialize in Nurse Immigration (i.e., obtaining "Nurse Green Cards").</p>
    <p>Many of the International Nurse Recruiters listed below also assist foreign nurses in preparing for the NLQX exam, ELPT and obtaining CGFNR and VisaCheck certificates.</p>
    <p class="last">If there are any International Nurse Recruiters or Law firms specializing in international nurse immigration that I have missed, please let me know (e-mail address is below), and I will add them to this Directory!</p>
    <a class="see-more" href="#">..see more</a>
  </div>
</section>

<section class="news">
  <h2>News Feed</h2>
  <p class="news-item first indent">GREAT NEWS! There is now a professional organization for International Nurses. This organization is called the Northbridge Association of Foreign Educated Nurses. Please visit their web site at www.nbafen.example. We here at the Directory of International Nurse Recruiters welcome this news.</p>
  <p class="news-item second indent">There is now a professional organization for International Nurses. This organization is called the Northbridge Association of Foreign Educated Nurses. Please visit their site.</p>
  <a class="read-more first" href="#">..read more</a>
  <a class="read-more second" href="#">..read more</a>
</section>

<footer class="site-footer">
  <p class="copyright"><strong>Valdoriel™</strong><br>All copyrights reserved®</p>
  <span class="footer-contact-label">Contact Us</span>
  <address class="footer-contact">TÉL. (555) 302-4419<br>TÉLEC. (555) 302-9154<br>1187 boulevard Ormelande, suite 3400<br>St-Hubert (Québec), K8W 5M3</address>
  <div class="social">
    Follow / Like us on
    <div class="social-links">
      <a href="https://friendwall.example/valdoriel-agence-de-placement" aria-label="Page sociale"></a>
      <a class="second" href="https://chirpline.example/Valdoriel" aria-label="Fil d'actualités"></a>
    </div>
  </div>
</footer>
</body>
</html>
```